Accounting and Financial Services Firm - Modern, Fresh, Original, Professional

We need a business card designed. We would like to see use of the the colors blue. Logo attached.

Modern, Fresh, Original, Professional,
Updates

Email section on business card required. design brief updated.

Target Market(s)

Small to medium businesses and high net worth individuals

Industry/Entity Type

Public Accounting

Contact Information for Business Card

Business Name: PM Ledgerline Chartered Accountants
Address: Level 14, 82 Harrow Lane Sydney NSW 2000
Ph: 02 9314 2587
Mobile: 04 XXXX XXXX
Email: anna@pmledgerline.com.au
Wechat ID: XXXXXXX
Website: www.pmledgerline.com.au

Name: Anna Petrov
Position: Manager

Font styles to use
Sans Serif

Colors
0492cd
33a6d7
85cae6

Requirements
Must have
• Modern font.

```html
<!DOCTYPE html>
<html lang="en">
<head>
<meta charset="utf-8">
<title>PM Ledgerline Chartered Accountants — Business Card</title>
<link href="https://fonts.googleapis.com/css2?family=Roboto:wght@400;500&family=Roboto+Condensed:wght@400;700&display=swap" rel="stylesheet">
<style>
  :root {
    --blue: #0492cd;
    --blue-mid: #33a6d7;
    --blue-light: #85cae6;
    --paper: #f4f4f4;
    --ink: #4a4a4a;
    --grey: #9a9a9a;
    --rule: #6e6e6e;
    --backdrop: #e9ebed;
  }
  * { box-sizing: border-box; margin: 0; padding: 0; }
  html, body { width: 1200px; height: 960px; overflow: hidden; }
  body {
    background: var(--backdrop);
    font-family: "Roboto", Arial, sans-serif;
    position: relative;
  }
  .card {
    position: absolute;
    width: 600px;
    height: 342px;
    overflow: hidden;
  }
  .card--front { left: 314px; top: 113px; background: var(--paper); }
  .card--back { left: 311px; top: 472px; background: var(--blue); }

  .brand { position: absolute; color: var(--blue); font-weight: 500; }
  .card--front .brand { left: 38px; top: 112px; }
  .brand__name { display: block; font-size: 34px; line-height: 1; letter-spacing: 0.5px; text-transform: uppercase; }
  .brand__tagline { display: block; font-size: 10px; letter-spacing: 2px; text-transform: uppercase; margin-top: 6px; padding-left: 32px; }
  .brand__mark { display: inline-block; width: 14px; height: 14px; background: var(--blue); margin-right: 8px; vertical-align: 4px; }

  .person { position: absolute; right: 37px; top: 186px; text-align: right; font-family: "Roboto Condensed", Arial, sans-serif; }
  .person__name { font-size: 23px; font-weight: 700; color: var(--blue); line-height: 1; text-transform: uppercase; }
  .person__role { font-size: 17px; color: var(--grey); margin-top: 3px; text-transform: uppercase; letter-spacing: 0.5px; }
  .tab { position: absolute; right: 0; top: 190px; width: 14px; height: 36px; background: var(--blue); }

  .divider { position: absolute; left: 38px; top: 236px; width: 525px; height: 1px; background: var(--rule); }

  .contacts { position: absolute; left: 38px; top: 246px; list-style: none; font-size: 15px; color: var(--ink); }
  .contacts li { height: 19px; display: flex; align-items: center; }
  .contacts svg { width: 14px; height: 14px; margin-right: 7px; fill: var(--blue); flex: none; }

  .address { position: absolute; right: 37px; top: 285px; text-align: right; font-size: 15px; line-height: 19px; color: var(--ink); font-style: normal; }

  .card--back .brand { left: 0; right: 0; top: 192px; text-align: center; color: #fff; }
  .card--back .brand__name { font-size: 34px; }
  .card--back .brand__tagline { padding-left: 0; font-size: 11px; }
  .website { position: absolute; left: 0; right: 0; top: 292px; text-align: center; color: #fff; font-size: 14px; letter-spacing: 3.4px; }
</style>
</head>
<body>
  <section class="card card--front">
    <div class="brand">
      <span class="brand__name"><span class="brand__mark"></span>PM Ledgerline</span>
      <span class="brand__tagline">Chartered Accountants</span>
    </div>

    <div class="person">
      <p class="person__name">Anna Petrov</p>
      <p class="person__role">Manager</p>
    </div>
    <div class="tab"></div>
    <div class="divider"></div>

    <ul class="contacts">
      <li><svg viewBox="0 0 16 16"><path d="M3.5 1l3 3-1.6 1.8a9 9 0 0 0 5.3 5.3L12 9.5l3 3-2 2.5C7 15 1 9 1 3z"/></svg>02 9314 2587</li>
      <li><svg viewBox="0 0 16 16"><path d="M4 0h8a1 1 0 0 1 1 1v14a1 1 0 0 1-1 1H4a1 1 0 0 1-1-1V1a1 1 0 0 1 1-1zm1 2v10h6V2zm3 11a1 1 0 1 0 0 2 1 1 0 0 0 0-2z"/></svg>0412 758 340</li>
      <li><svg viewBox="0 0 16 16"><rect x="1" y="1" width="14" height="14" rx="2"/></svg>0412758340</li>
      <li><svg viewBox="0 0 16 16"><path d="M1 3h14v10H1zm1.2 1.2L8 8.6l5.8-4.4z" fill-rule="evenodd"/></svg>anna@pmledgerline.com.au</li>
    </ul>

    <address class="address">Level 14, 82 Harrow Lane<br>Sydney NSW 2000</address>
  </section>

  <section class="card card--back">
    <div class="brand">
      <span class="brand__name">PM Ledgerline</span>
      <span class="brand__tagline">Chartered Accountants</span>
    </div>
    <p class="website">www.pmledgerline.com.au</p>
  </section>
</body>
</html>
```